Web Design Project

We need a web design new company based in Australia. We're a search engine marketing company who predominantly manages Vexora bidlines campaigns.
Currently still deciding on a business name so lets use “Marlow Tappers” for now.
Target market....
small to medium size businesses
- more clicks to their website from the 1st page of Vexora
- more relevant, (higher quality) clicks
- higher return on investment from their bidlines campaign
- more sales, leads, (conversions)
We'd like clean, simple, semi-professional as we'd like to pick up some high end corporate clients.
A website that we love the look and feel of – but they’re a direct competitor so can’t be too similar in design.
http://www.brindlepath.com.au/search-engine-marketing.html
**please check portfolio on this web page..they designs are absolutely stunning!! http://www.brindlepath.com.au/website-design.html
Updates
Please refer to the attached file, a rough sketch of my web page.
place replace...."Afraid your bidlines campaign is underperforming with,....
Industry/Entity Type
Business
Look and feel

```html
<!DOCTYPE html>
<html lang="en">
<head>
<meta charset="utf-8">
<title>Marlow Tappers – Search Engine Marketing</title>
<link href="https://fonts.googleapis.com/css2?family=Ubuntu:wght@400;500&family=Ubuntu+Condensed&family=Mulish:wght@700;800&family=Questrial&family=Arimo&display=swap" rel="stylesheet">
<style>
:root{
  --blue-deep:#0a4fc4;
  --blue-mid:#1466dd;
  --blue-light:#2a8ff0;
  --brand-blue:#0a67c0;
  --nav-dark:#1c1c1c;
  --nav-line:#4a4a4a;
  --hero-bg:#f6f6f7;
  --ink:#222222;
  --ink-soft:#555555;
  --orange:#f26a0f;
  --white:#ffffff;
  --footer:#1f1f1f;
  --art-grey:#e2e2e2;
  --art-blue:#5aa6ea;
}
*{margin:0;padding:0;box-sizing:border-box}
html,body{width:1200px;height:1136px;overflow:hidden}
body{position:relative;background:linear-gradient(160deg,var(--blue-light) 0%,var(--blue-mid) 30%,var(--blue-deep) 100%);font-family:"Arimo",Arial,sans-serif}
.top-strip{position:absolute;left:0;top:0;width:1200px;height:9px;background:#0b1a33}
.header-swoosh{position:absolute;left:0;top:0;width:1200px;height:200px}
.logo{position:absolute;left:36px;top:50px;font-family:"Ubuntu",sans-serif;font-weight:500;font-size:40px;color:var(--white);letter-spacing:.2px}
.phone{position:absolute;left:945px;top:58px;display:flex;align-items:center;gap:6px;font-family:"Ubuntu",sans-serif;font-size:30px;color:var(--white)}
.main-nav{position:absolute;left:23px;top:131px;width:1151px;height:61px;background:linear-gradient(#2e2e2e,#141414);display:flex;border-bottom:3px solid #6a6a6a}
.main-nav a{display:flex;align-items:center;justify-content:center;height:100%;color:var(--white);text-decoration:none;font-family:"Ubuntu Condensed","Ubuntu",sans-serif;font-size:19px;border-right:1px solid var(--nav-line)}
.main-nav a:last-child{border-right:none}
.main-nav a.active{background:linear-gradient(#4a4a4a,#2a2a2a)}
.hero{position:absolute;left:23px;top:192px;width:1151px;height:310px;background:linear-gradient(#ffffff,var(--hero-bg))}
.hero-title{position:absolute;left:38px;top:50px;font-family:"Mulish",sans-serif;color:var(--ink)}
.hero-title .line-1{display:block;font-size:45px;font-weight:800;line-height:1}
.hero-title .line-2{display:block;font-size:26px;font-weight:800;margin-top:12px}
.hero-chevron{position:absolute;left:548px;top:65px}
.check-title{position:absolute;left:645px;top:54px;font-family:"Questrial",sans-serif;font-size:33px;color:var(--ink);line-height:42px}
.check-title strong{color:var(--brand-blue);font-family:"Mulish",sans-serif;font-weight:800}
.url-field{position:absolute;left:640px;top:157px;width:466px;height:48px;border-radius:4px;background:linear-gradient(#e4e4e6,#eeeeef);color:#888;font-family:"Questrial",sans-serif;font-size:21px;padding:12px 18px}
.step-count{position:absolute;left:653px;top:226px;font-family:"Questrial",sans-serif;font-size:22px;color:#555;word-spacing:6px}
.next-btn{position:absolute;left:992px;top:218px;width:111px;height:46px;border-radius:3px;background:linear-gradient(#1a7ad6,var(--brand-blue));color:var(--white);font-family:"Mulish",sans-serif;font-weight:800;font-size:19px;display:flex;align-items:center;justify-content:center}
.services{position:absolute;left:23px;top:502px;width:1151px;height:541px;background:var(--white)}
.service{position:absolute;top:34px;width:320px}
.service h2{font-family:"Questrial",sans-serif;font-weight:400;font-size:23px;color:var(--ink);margin-left:10px;height:42px}
.service-art{width:317px;height:187px;border:1px solid #d8d8d8;border-radius:4px}
.art-local{background:linear-gradient(180deg,#f4f4f4,var(--art-grey))}
.art-national{background:linear-gradient(180deg,#f2f6fb,#dce8f5)}
.art-ecommerce{background:linear-gradient(180deg,#e6f1fc,var(--art-blue))}
.service h3{margin-top:26px;font-family:"Arimo",sans-serif;font-weight:400;font-size:18px;color:var(--orange);margin-left:6px}
.service p{margin:6px 0 0 6px;width:314px;font-size:14.2px;line-height:23.4px;color:var(--ink-soft);text-align:justify}
.learn-btn{display:inline-block;margin:16px 0 0 6px;padding:7px 13px;border-radius:3px;background:var(--brand-blue);color:var(--white);font-size:15.5px;text-decoration:none}
.site-footer{position:absolute;left:23px;top:1043px;width:1151px;height:93px;background:var(--footer);color:var(--white);font-size:13.5px}
.copyright{position:absolute;left:33px;top:21px}
.footer-nav{position:absolute;right:28px;top:19px;display:flex}
.footer-nav a{color:var(--white);text-decoration:none;padding:0 9px;border-left:1px solid #bbb;line-height:14px}
.footer-nav a:first-child{border-left:none}
.footer-nav a:last-child{padding-right:0}
</style>
</head>
<body>
<div class="top-strip"></div>
<svg class="header-swoosh" viewBox="0 0 1200 200" aria-hidden="true">
  <path d="M0 9 H1200 V180 C1000 120 800 80 560 95 C380 105 180 70 0 40 Z" fill="#0d55c9" opacity=".55"/>
  <path d="M600 9 C800 60 1000 60 1200 40 V9 Z" fill="#2b9be8" opacity=".45"/>
</svg>

<header>
  <div class="logo">Marlow Tappers</div>
  <div class="phone">
    <svg width="26" height="40" viewBox="0 0 26 40" aria-hidden="true"><path d="M6 2 L12 2 L13 12 L8 14 C8 22 11 28 16 32 L20 28 L25 34 L20 39 C8 36 1 22 2 8 Z" fill="none" stroke="#fff" stroke-width="2.4" stroke-linejoin="round"/></svg>
    <span>1300 555 0148</span>
  </div>
</header>

<nav class="main-nav">
  <a class="active" href="#" style="width:159px">Home</a>
  <a href="#" style="width:147px">About</a>
  <a href="#" style="width:211px">Vexora Bidlines</a>
  <a href="#" style="width:199px">Other Services</a>
  <a href="#" style="width:223px">Why Choose Us?</a>
  <a href="#" style="width:212px">Contact Us</a>
</nav>

<section class="hero">
  <h1 class="hero-title"><span class="line-1">Afraid your bidlines</span><span class="line-2">campaign is understandperforming?</span></h1>
  <svg class="hero-chevron" width="46" height="76" viewBox="0 0 46 76" aria-hidden="true"><path d="M0 0 H20 L46 38 L20 76 H0 L26 38 Z" fill="#0a67c0"/></svg>
  <div class="check-title"><strong>FREE</strong> Bidlines Health Check<br>Step1: Your Website</div>
  <div class="url-field">http://</div>
  <div class="step-count">Step 1 of 3</div>
  <div class="next-btn">NEXT</div>
</section>

<main class="services">
  <article class="service" style="left:30px">
    <h2>Local Bidlines</h2>
    <div class="service-art art-local" role="img" aria-label="Illustration for local search marketing"></div>
    <h3>Lorem ipsum dolor sit amet</h3>
    <p>consectetuer adipiscing elit. Nam cursus. Morbi ut mi. Nullam enim leo, egestas id, condimentum at, laoreet mattis, massa. Sed eleifend nonummy diam. Praesent mauris ante, elementum et, bibendum at</p>
    <a class="learn-btn" href="#">learn more</a>
  </article>
  <article class="service" style="left:414px">
    <h2>National Bidlines</h2>
    <div class="service-art art-national" role="img" aria-label="Illustration for national search marketing"></div>
    <h3>Lorem ipsum dolor sit amet</h3>
    <p>consectetuer adipiscing elit. Nam cursus. Morbi ut mi. Nullam enim leo, egestas id, condimentum at, laoreet mattis, massa. Sed eleifend nonummy diam. Praesent mauris ante, elementum et, bibendum at</p>
    <a class="learn-btn" href="#">learn more</a>
  </article>
  <article class="service" style="left:804px">
    <h2>Ecommerce Bidlines</h2>
    <div class="service-art art-ecommerce" role="img" aria-label="Illustration for ecommerce search marketing"></div>
    <h3>Lorem ipsum dolor sit amet</h3>
    <p>consectetuer adipiscing elit. Nam cursus. Morbi ut mi. Nullam enim leo, egestas id, condimentum at, laoreet mattis, massa. Sed eleifend nonummy diam. Praesent mauris ante, elementum et, bibendum at</p>
    <a class="learn-btn" href="#">learn more</a>
  </article>
</main>

<footer class="site-footer">
  <div class="copyright">© 2012 Company Name &nbsp;| All right reserved</div>
  <nav class="footer-nav">
    <a href="#">Home</a><a href="#">About</a><a href="#">Vexora Bidlines</a><a href="#">Other Services</a><a href="#">Why Choose Us?</a><a href="#">Contact Us</a>
  </nav>
</footer>
</body>
</html>
```